Firm of surveyors needs a professional yet friendly looking flyer

Our company offers help to landlords who have a phone mast on their property. We help them to negotiate the best rent and lease terms. There are so many landlords who don't seek professional advice because they don't know it's available. We want to send them a flyer which is informative, looks professional but also friendly so it prompts them to call us. I have attached the wording and some pictures but have more I can send but they were too large to attach.

Target Market(s)

Ranges from farmers to large corporations and land owners

Industry/Entity Type

Surveyor

Font styles to use
Sans Serif

Colors
acd136
9bcb3c
000000
ffffff
606060
848484

Requirements
Must have
• Must be clear, must give a professional look, must include pictures, must include our logo, must use our colour scheme (or variations of it). Ideally, I would like a try-fold design if possible.
Nice to have
• I would like there to be stand out lines to catch the readers eye (I have included some on the wording document). I would like a clean and modern design
Should not have
• Should not be too fussy

```html
<!DOCTYPE html>
<html lang="en">
<head>
<meta charset="utf-8">
<title>Signal Acre Surveyors – Landlord Tri-fold</title>
<link rel="stylesheet" href="https://fonts.googleapis.com/css2?family=Montserrat:wght@600;800&family=Mulish:wght@400;700&display=swap">
<style>
  :root {
    --lime: #acd136;
    --leaf: #9bcb3c;
    --forest: #4a6b2a;
    --olive: #8ea45c;
    --olive-light: #a9bb7c;
    --ink: #000000;
    --paper: #ffffff;
    --grey-dark: #606060;
    --grey-mid: #848484;
    --backdrop: #4e4e4e;
    --shade: #555555;
  }
  * { box-sizing: border-box; margin: 0; padding: 0; }
  html, body { width: 1200px; height: 1200px; overflow: hidden; }
  body { background: var(--backdrop); position: relative; font-family: "Mulish", Arial, sans-serif; }

  .spread { position: absolute; left: 195px; width: 810px; height: 585px; background: var(--paper); overflow: hidden; }
  .spread--outside { top: 8px; }
  .spread--inside { top: 607px; }
  .spread__shapes { position: absolute; inset: 0; width: 810px; height: 585px; }
  .fold { stroke: rgba(0,0,0,.08); stroke-width: 1; }

  .block { position: absolute; }
  .copy { font-size: 7.3px; line-height: 1.42; color: var(--grey-dark); }
  .copy--light { color: var(--paper); }
  .copy strong { font-weight: 700; }

  .section-title { font-family: "Montserrat", Arial, sans-serif; font-weight: 800; color: var(--forest); font-size: 12px; margin-bottom: 7px; }

  /* outside */
  .intro { left: 26px; top: 30px; width: 222px; color: var(--paper); font-size: 11.4px; line-height: 1.33; }
  .intro__callout { margin-top: 10px; font-family: "Montserrat", Arial, sans-serif; font-weight: 800; font-size: 11px; line-height: 1.4; }
  .services { left: 26px; top: 300px; }
  .services__list { list-style: none; color: var(--grey-dark); font-size: 12px; line-height: 1.6; }
  .services__list li::before { content: "• "; }

  .contact { left: 372px; top: 372px; width: 150px; }
  .contact__list { list-style: none; }
  .contact__item { display: flex; align-items: flex-start; gap: 7px; font-size: 9px; line-height: 1.35; color: var(--grey-dark); margin-bottom: 9px; }
  .contact__icon { flex: 0 0 14px; width: 14px; height: 14px; border-radius: 50%; background: var(--forest); display: flex; align-items: center; justify-content: center; }
  .contact__icon svg { width: 8px; height: 8px; fill: var(--paper); }

  .brand { left: 585px; top: 40px; display: flex; align-items: center; gap: 8px; }
  .brand__mark { width: 18px; height: 18px; border-radius: 50%; background: var(--forest); }
  .brand__name { font-family: "Montserrat", Arial, sans-serif; font-weight: 800; color: var(--forest); font-size: 17px; line-height: 1.05; }
  .cover-headline { left: 562px; top: 196px; width: 128px; font-family: "Montserrat", Arial, sans-serif; font-weight: 800; color: var(--forest); font-size: 17.5px; line-height: 1.32; text-transform: uppercase; }
  .cover-headline__sub { display: block; margin-top: 2px; font-size: 11.5px; line-height: 1.4; }

  /* inside */
  .about { left: 27px; top: 30px; width: 218px; }
  .review { left: 300px; top: 28px; width: 222px; }
  .climate-note { left: 575px; top: 45px; width: 210px; }
  .stamp { left: 238px; top: 280px; width: 158px; font-family: "Montserrat", Arial, sans-serif; font-weight: 800; font-size: 12.2px; line-height: 1.36; color: var(--lime); text-transform: uppercase; }
  .stamp span { background: var(--forest); padding: 0 3px; box-decoration-break: clone; -webkit-box-decoration-break: clone; }
  .offer { left: 556px; top: 238px; width: 118px; font-family: "Montserrat", Arial, sans-serif; font-weight: 800; font-size: 11.5px; line-height: 1.42; color: var(--paper); text-transform: uppercase; }
  .col-sell { left: 27px; top: 455px; width: 218px; }
  .col-get { left: 300px; top: 462px; width: 218px; }
  .col-climate { left: 567px; top: 421px; width: 215px; }
</style>
</head>
<body>

<!-- Outside of the tri-fold -->
<section class="spread spread--outside" aria-label="Flyer outside">
  <svg class="spread__shapes" viewBox="0 0 810 585">
    <defs>
      <linearGradient id="hillMast" x1="0" y1="0" x2="0" y2="1">
        <stop offset="0" stop-color="#e4e4e4"/>
        <stop offset=".45" stop-color="#b9b9b9"/>
        <stop offset=".78" stop-color="#8d8d8d"/>
        <stop offset=".9" stop-color="#6f6f6f"/>
        <stop offset=".94" stop-color="#7f9a4a"/>
        <stop offset="1" stop-color="#8fb548"/>
      </linearGradient>
      <radialGradient id="oliveGlow" cx=".55" cy=".35" r=".7">
        <stop offset="0" stop-color="var(--olive-light)"/>
        <stop offset="1" stop-color="var(--olive)"/>
      </radialGradient>
    </defs>
    <g role="img" aria-label="Photo of a lattice phone mast on a hillside">
      <polygon points="539,192 810,80 810,585 539,585" fill="url(#hillMast)"/>
    </g>
    <polygon points="539,192 565,182 565,585 539,585" fill="#8a8a8a"/>
    <g role="img" aria-label="Photo of mast antennas, green tinted">
      <polygon points="255,0 539,0 539,192 272,326" fill="url(#oliveGlow)"/>
    </g>
    <polygon points="305,282 272,326 262,262" fill="var(--shade)"/>
    <polygon points="0,0 262,0 305,282 0,256" fill="var(--forest)"/>
    <line class="fold" x1="263" y1="0" x2="263" y2="585"/>
    <line class="fold" x1="539" y1="0" x2="539" y2="585"/>
  </svg>

  <div class="block intro">
    <p>In April 2017, the Government introduced the Digital Economy Act. This sets out significant changes for landlords, including the way rents are calculated. We have already seen operators contact landlords, trying to reduce their rent in light of this new law. We are working alongside specialist telecoms solicitors to try to reduce the potential negative impact on landlords.</p>
    <p class="intro__callout">Landlords should not sign anything until they have sought professional advice</p>
  </div>

  <div class="block services">
    <h2 class="section-title">Our Services</h2>
    <ul class="services__list">
      <li>Rent Reviews</li>
      <li>Lease Renewals</li>
      <li>Site Sales</li>
      <li>Lease Advice</li>
    </ul>
  </div>

  <div class="block contact">
    <h2 class="section-title">Contact Us</h2>
    <ul class="contact__list">
      <li class="contact__item">
        <span class="contact__icon"><svg viewBox="0 0 10 10"><path d="M2.2 0.6l1.6 1.7-0.9 1.2c0.6 1.3 1.5 2.2 2.8 2.8l1.2-0.9 1.7 1.6-1 1.9C4.2 8.6 1.2 5.6 0.4 1.6z"/></svg></span>
        <span>01632 960 418</span>
      </li>
      <li class="contact__item">
        <span class="contact__icon"><svg viewBox="0 0 10 10"><path d="M0.5 2h9v6h-9z M1 2.5l4 3 4-3" fill="none" stroke="#fff" stroke-width="1"/></svg></span>
        <span>hello@signalacre.example</span>
      </li>
      <li class="contact__item">
        <span class="contact__icon"><svg viewBox="0 0 10 10"><path d="M5 0.5a3.2 3.2 0 0 1 3.2 3.2C8.2 6 5 9.5 5 9.5S1.8 6 1.8 3.7A3.2 3.2 0 0 1 5 0.5zm0 2a1.2 1.2 0 1 0 0 2.4 1.2 1.2 0 0 0 0-2.4z"/></svg></span>
        <span>Unit 4, Moor Lane<br>Halden HD9 4QX</span>
      </li>
      <li class="contact__item">
        <span class="contact__icon"><svg viewBox="0 0 10 10"><circle cx="5" cy="5" r="4" fill="none" stroke="#fff" stroke-width="1"/><path d="M1 5h8M5 1c-2 2.5-2 5.5 0 8M5 1c2 2.5 2 5.5 0 8" fill="none" stroke="#fff" stroke-width=".8"/></svg></span>
        <span>www.signalacre.example</span>
      </li>
    </ul>
  </div>

  <div class="block brand">
    <span class="brand__mark"></span>
    <span class="brand__name">Signal Acre<br>Surveyors</span>
  </div>

  <h1 class="block cover-headline">Unsure whether you are getting the best rent?
    <span class="cover-headline__sub">Call us for a free, no obligation consultation</span>
  </h1>
</section>

<!-- Inside of the tri-fold -->
<section class="spread spread--inside" aria-label="Flyer inside">
  <svg class="spread__shapes" viewBox="0 0 810 585">
    <defs>
      <linearGradient id="mastHead" x1="0" y1="0" x2="1" y2="1">
        <stop offset="0" stop-color="#9c9c9c"/>
        <stop offset=".5" stop-color="#bdbdbd"/>
        <stop offset="1" stop-color="#7a7a7a"/>
      </linearGradient>
      <linearGradient id="moorland" x1="0" y1="0" x2="0" y2="1">
        <stop offset="0" stop-color="#8f8f8f"/>
        <stop offset=".35" stop-color="#cfcfcf"/>
        <stop offset=".78" stop-color="#a4a4a4"/>
        <stop offset=".86" stop-color="#7d7d7d"/>
        <stop offset=".92" stop-color="#6f8a45"/>
        <stop offset="1" stop-color="#8fb548"/>
      </linearGradient>
      <linearGradient id="monopole" x1="0" y1="0" x2="1" y2="0">
        <stop offset="0" stop-color="#8a8a8a"/>
        <stop offset=".6" stop-color="#a6a6a6"/>
        <stop offset="1" stop-color="#909090"/>
      </linearGradient>
    </defs>
    <g role="img" aria-label="Photo of a mast head with antennas and a platform">
      <rect x="0" y="150" width="269" height="262" fill="url(#mastHead)"/>
    </g>
    <rect x="0" y="410" width="269" height="14" fill="var(--forest)"/>
    <g role="img" aria-label="Photo of a lattice mast on moorland">
      <rect x="269" y="180" width="272" height="243" fill="url(#moorland)"/>
    </g>
    <rect x="269" y="415" width="272" height="10" fill="var(--forest)"/>
    <g role="img" aria-label="Photo of a monopole mast with antennas and a dish">
      <rect x="541" y="120" width="269" height="300" fill="url(#monopole)"/>
    </g>
    <rect x="541" y="375" width="269" height="14" fill="var(--forest)"/>
    <polygon points="541,0 810,0 810,128 562,228 541,232" fill="var(--forest)"/>
    <polygon points="0,0 269,0 277,150 0,184" fill="var(--lime)"/>
    <polygon points="530,196 575,190 555,230" fill="var(--shade)"/>
    <polygon points="269,0 545,0 575,190 360,208 240,196 277,150" fill="var(--leaf)"/>
    <line class="fold" x1="269" y1="0" x2="269" y2="585"/>
    <line class="fold" x1="541" y1="0" x2="541" y2="585"/>
  </svg>

  <p class="block copy copy--light about"><strong>Signal Acre Surveyors is a firm of telecoms surveyors with over 15 years' experience of dealing with mobile phone mast operators.</strong> We have built up a massive database of thousands of comparable mobile phone mast deals to aid us in our telecoms negotiations. All our surveyors have spent time working for phone mast operators and know the industry inside out. We now work <strong>exclusively for landlords</strong>, fighting your corner, ensuring our landlords get the highest rents and best lease terms available in the market place.</p>

  <p class="block copy copy--light review">Many of the original mobile phone mast leases / agreements are now coming up for renewal. This is an ideal opportunity for landlords to achieve the best deal. <strong>We are currently offering to review telecoms leases for free and provide landlords with our recommendations.</strong> If you would like to take us up on this free no obligation offer, send a copy of your agreement and any recent correspondence to us, either via post or email using the details on this flyer. Please also provide us with your name, contact number and let us know the current rent you are achieving so we can see if there is room for improvement. Once we have received this, one of our surveyors will give you a call when convenient to talk through your lease with you, highlighting anything we feel needs addressing, any opportunity to increase the rent, or to discuss a specific issue you are having with your mast (i.e. an upgrade request).</p>

  <p class="block copy copy--light climate-note">Recently, operators have been attempting to cut costs by reducing rents. They are joining forces in an effort to drive rents down. Many landlords are contacting us after receiving a letter from the operators / operator's agent, telling them they must accept a rent reduction or risk losing their site. In the majority of cases, Signal Acre Surveyors can prevent this from occurring and protect the landlord's rental income.</p>

  <p class="block stamp"><span>Our expert surveyors will be to help you understand proposed changes and what they could mean for you</span></p>

  <p class="block offer">In selling your site? Or already have an offer? We can help you to achieve the best sale price, quickly</p>

  <div class="block col-sell">
    <h2 class="section-title">Sell your phone mast</h2>
    <p class="copy">We can also assist landlords in selling their phone mast. We have strong links with many large investors who regularly purchase the freehold or leasehold interest of masts and will pay a cash lump sum of tens, even hundreds of thousands of pounds. This can be done in a matter of weeks and the cash is yours to spend however you like, regardless of whether the mast stays for the duration of the investors leasehold or not. We can negotiate flexible terms, such as a buyback option so please call us today to discuss.</p>
  </div>

  <div class="block col-get">
    <h2 class="section-title">Getting a phone mast</h2>
    <p class="copy">If you don't currently have a mast located on your land but are interested in receiving thousands of pounds a year in rental income, or you have a redundant mast you would like to market, we offer a free advertising service on our website. We will market your land to phone mast operators with a view to having a mast located there. Please visit the 'Advertise My Site' link on our website to take advantage of this service.</p>
  </div>

  <div class="block col-climate">
    <h2 class="section-title">The current telecoms climate</h2>
    <p class="copy">The telecoms market, in relation to mobile phone masts, is going through some huge changes. Operators are combining to cut costs. We have already seen Triad Mobile join forces with Vocalis to form CellShare Ltd. More recently, Tessera and Oxen Mobile form a jointly owned company, and Amber have merged to form AllConnect Ltd to become the new network leader. What this can mean for the landlord is changes to their site and potentially the loss of income. It can all be very confusing but don't worry, this is where we can help. We know the telecoms industry and understand how a new situation may affect a landlord, therefore, allowing us to provide the best advice on protecting your asset.</p>
  </div>
</section>

</body>
</html>
```